Personal Business Card design contest for freelance work

Include

Proflink.example/in/DanielMWhitacre (as URL and/or QR Code)
Daniel Whitacre
(555) 014-2938
DanielMWhitacre@Mailnest.example
Lakemont, TX

Industry/Entity Type

Business

```html
<!DOCTYPE html>
<html lang="en">
<head>
<meta charset="utf-8">
<title>Daniel Whitacre — Business Card</title>
<link href="https://fonts.googleapis.com/css2?family=Ubuntu:wght@400;700&display=swap" rel="stylesheet">
<style>
  :root {
    --backdrop: #d9d9d9;
    --card: #f4f4f2;
    --stripe: #8f6337;
    --stripe-text: #ffffff;
    --ink: #1c1c1c;
    --art-light: #e8e2da;
    --art-skin: #d9a77c;
    --art-suit: #2f2f31;
  }
  html, body {
    margin: 0;
    width: 1200px;
    height: 1000px;
    overflow: hidden;
    background: var(--backdrop);
    font-family: "Ubuntu", sans-serif;
  }
  .business-card {
    position: absolute;
    left: 100px;
    top: 214px;
    width: 1000px;
    height: 571px;
    background: var(--card);
    box-shadow: 0 6px 18px rgba(0,0,0,0.18);
    overflow: hidden;
  }
  .portrait-art {
    position: absolute;
    left: 120px;
    top: 90px;
    width: 300px;
    height: 380px;
    border-radius: 16px;
    background: linear-gradient(180deg, var(--art-light) 0%, var(--art-skin) 30%, var(--art-suit) 50%, var(--art-suit) 92%, var(--art-light) 100%);
    opacity: 0.8;
  }
  .stripe,
  .profile-link {
    position: absolute;
    top: 0;
    height: 571px;
    box-sizing: border-box;
    writing-mode: vertical-rl;
    transform: rotate(180deg);
    text-align: start;
    white-space: nowrap;
  }
  .stripe {
    background: var(--stripe);
    color: var(--stripe-text);
  }
  .stripe-name  { left: 515px; width: 82px; line-height: 82px; font-weight: 700; font-size: 31px; padding-top: 40px; }
  .stripe-phone { left: 638px; width: 54px; line-height: 54px; font-size: 23px; padding-top: 60px; }
  .stripe-email { left: 728px; width: 54px; line-height: 54px; font-size: 21px; padding-top: 40px; }
  .stripe-city  { left: 818px; width: 54px; line-height: 54px; font-size: 23px; padding-top: 230px; }
  .profile-link {
    left: 905px;
    width: 54px;
    line-height: 54px;
    padding-top: 30px;
    color: var(--ink);
    font-size: 24px;
    letter-spacing: 0.5px;
  }
</style>
</head>
<body>
  <main class="business-card">
    <div class="portrait-art" role="img" aria-label="Caricature illustration of a smiling man in a dark suit and striped tie holding a laptop"></div>
    <div class="stripe stripe-name">Daniel Whitacre</div>
    <div class="stripe stripe-phone">Phone: (555) 014-2938</div>
    <div class="stripe stripe-email">Email: DanielMWhitacre@Mailnest.example</div>
    <div class="stripe stripe-city">Lakemont, TX</div>
    <div class="profile-link">Proflink.example/in/DanielMWhitacre</div>
  </main>
</body>
</html>
```